Business Cards for a law firm

Business cards for our law firm. Use our silhoette logo and OAK HARBOR - check our website (www.oakharbor-legal.com)

Contact Information for Business Card

our silhouette logo, OAK HARBOR, 800-555-0147, Dorian Kestrup, dorian@oakharbor-legal.com

Requirements
Must have
• our silhouette logo, OAK HARBOR, 800-555-0147, Dorian Kestrup, dorian@oakharbor-legal.com

```html
<!DOCTYPE html>
<html lang="en">
<head>
<meta charset="utf-8">
<title>Oak Harbor – Business Cards</title>
<link rel="stylesheet" href="https://fonts.googleapis.com/css2?family=Work+Sans:wght@500;600;700&display=swap">
<style>
  :root {
    --navy: #1b3169;
    --gold: #f3a41d;
    --panel-grey: #e4e4e6;
    --page: #f2f2f2;
    --card: #ffffff;
    --white: #ffffff;
  }
  * { margin: 0; padding: 0; box-sizing: border-box; }
  html, body { width: 1100px; height: 1200px; overflow: hidden; }
  body {
    background: var(--page);
    font-family: "Work Sans", Arial, sans-serif;
    position: relative;
  }
  .card {
    position: absolute;
    left: 115px;
    width: 869px;
    height: 474px;
    background: var(--card);
    overflow: hidden;
  }
  .card--front { top: 63px; }
  .card--back { top: 662px; }

  .brand-mark { background: var(--navy); flex: none; }
  .brand-text {
    display: flex;
    flex-direction: column;
    align-items: center;
  }
  .brand-name {
    color: var(--navy);
    font-weight: 600;
    letter-spacing: 0.06em;
    line-height: 1;
    white-space: nowrap;
  }
  .brand-tagline {
    color: var(--gold);
    font-weight: 600;
    line-height: 1;
    white-space: nowrap;
  }

  /* Front */
  .front-brand {
    position: absolute;
    top: 212px;
    left: 0;
    width: 100%;
    display: flex;
    justify-content: center;
    align-items: center;
    gap: 24px;
  }
  .front-brand .brand-mark { width: 56px; height: 56px; }
  .front-brand .brand-name { font-size: 58px; }
  .front-brand .brand-tagline {
    font-size: 24px;
    letter-spacing: 0.38em;
    margin-top: 14px;
    padding-left: 0.38em;
  }
  .front-band {
    position: absolute;
    left: 23px;
    top: 431px;
    width: 822px;
    height: 30px;
    background: var(--navy);
  }

  /* Back */
  .back-header {
    position: absolute;
    left: 23px;
    top: 12px;
    width: 432px;
    height: 105px;
  }
  .back-header svg { position: absolute; inset: 0; }
  .back-brand {
    position: absolute;
    left: 52px;
    top: 0;
    height: 105px;
    display: flex;
    align-items: center;
    gap: 16px;
  }
  .back-brand .brand-mark { width: 34px; height: 34px; }
  .back-brand .brand-name { font-size: 32px; }
  .back-brand .brand-tagline {
    font-size: 14px;
    letter-spacing: 0.36em;
    margin-top: 8px;
    padding-left: 0.36em;
  }

  .contact-list {
    position: absolute;
    left: 45px;
    top: 266px;
    width: 450px;
    list-style: none;
  }
  .contact-item {
    display: flex;
    align-items: center;
    gap: 10px;
    color: var(--gold);
    font-weight: 600;
    letter-spacing: 0.03em;
    line-height: 1;
    white-space: nowrap;
  }
  .contact-item svg { width: 20px; height: 20px; flex: none; }
  .contact-item--phone { font-size: 28px; }
  .contact-item--email { font-size: 21px; margin-top: 24px; }
  .contact-item--web { font-size: 19px; margin-top: 24px; }

  .partner-photo {
    position: absolute;
    left: 512px;
    top: 170px;
    width: 316px;
    height: 228px;
    background: linear-gradient(180deg, #eef0f3 0%, #b9bcc4 38%, #2a2d3a 62%, #22242f 100%);
  }
  .back-wave { position: absolute; left: 23px; top: 392px; }
  .partner-names {
    position: absolute;
    left: 503px;
    top: 419px;
    display: flex;
    gap: 16px;
    color: var(--white);
    font-size: 15px;
    font-weight: 700;
    letter-spacing: 0.08em;
    white-space: nowrap;
  }
</style>
</head>
<body>

<section class="card card--front">
  <div class="front-brand">
    <span class="brand-mark"></span>
    <div class="brand-text">
      <span class="brand-name">OAK HARBOR</span>
      <span class="brand-tagline">INJURY ATTORNEYS</span>
    </div>
  </div>
  <div class="front-band"></div>
</section>

<section class="card card--back">
  <div class="back-header">
    <svg width="432" height="105" viewBox="0 0 432 105">
      <path d="M0 0 H432 L410 80 Q403 105 380 105 H0 Z" fill="var(--panel-grey)"/>
    </svg>
    <div class="back-brand">
      <span class="brand-mark"></span>
      <div class="brand-text">
        <span class="brand-name">OAK HARBOR</span>
        <span class="brand-tagline">INJURY ATTORNEYS</span>
      </div>
    </div>
  </div>

  <ul class="contact-list">
    <li class="contact-item contact-item--phone">
      <svg viewBox="0 0 20 20"><circle cx="10" cy="10" r="10" fill="var(--navy)"/><path d="M6.6 5.2 L8.2 5 L9 7.6 L8 8.5 Q9 10.8 11.4 12 L12.4 11 L15 11.8 L14.8 13.4 Q14.5 14.6 13.2 14.6 Q9 14.3 6.2 10.6 Q5.2 8.8 5.4 6.6 Q5.6 5.4 6.6 5.2 Z" fill="var(--white)"/></svg>
      800-555-0147
    </li>
    <li class="contact-item contact-item--email">
      <svg viewBox="0 0 20 20"><circle cx="10" cy="10" r="10" fill="var(--navy)"/><rect x="5" y="6.5" width="10" height="7" fill="none" stroke="var(--white)" stroke-width="1.2"/><path d="M5 6.5 L10 10.5 L15 6.5" fill="none" stroke="var(--white)" stroke-width="1.2"/></svg>
      DORIAN@OAKHARBOR-LEGAL.COM
    </li>
    <li class="contact-item contact-item--web">
      <svg viewBox="0 0 20 20"><circle cx="10" cy="10" r="10" fill="var(--navy)"/><g fill="none" stroke="var(--white)" stroke-width="1"><circle cx="10" cy="10" r="5.5"/><ellipse cx="10" cy="10" rx="2.4" ry="5.5"/><path d="M4.5 10 H15.5 M5.3 7.3 H14.7 M5.3 12.7 H14.7"/></g></svg>
      WWW.OAKHARBOR-LEGAL.COM
    </li>
  </ul>

  <div class="partner-photo" role="img" aria-label="Portrait photo of the two partners in dark suits"></div>

  <svg class="back-wave" width="822" height="69" viewBox="0 0 822 69">
    <path d="M0 39 H180 C300 39 420 10 480 2 L490 0 H822 V69 H0 Z" fill="var(--navy)"/>
  </svg>
  <div class="partner-names">
    <span>DORIAN KESTRUP</span>
    <span>REID KESTRUP</span>
  </div>
</section>

</body>
</html>
```